Banner for promote service of debit card

We are PagaVelo and we need the banners to be posted on the facebook and instagram pages.
We want something to communicate that it is an exclusive debit card full of services.
Low commissions.
Our competitors:
https://www.nortapay-pagos.it/it/home.html
https://www.zelkor-conti.it/it/
https://www.fotoreelz.it/serravanbank/
sendquillo
maybe some banner that makes the idea of a convenient debit card that everyone can use.
Girls enjoying card shopping.
Please check also website for slogans and phrases to use
https://www.pagavelo-carta.it/
Should show the services.
We must convey that it is a fast, simple card that guarantees privacy.
We need strong banners that attract people as these ban will be sponsored on instagram and facebook
Target Market(s)
People 18-35 y
Open Bank account. low commissions. Easy to use. No limits. 100% Privacy.
Requirements
Must have
- Written in Italian.

```html
<!DOCTYPE html>
<html lang="it">
<head>
<meta charset="UTF-8">
<title>PagaVelo – Una carta per tutti</title>
<link rel="stylesheet" href="https://fonts.googleapis.com/css2?family=Montserrat:wght@600;700&display=swap">
<style>
  :root {
    --page-bg: #ffffff;
    --photo-light: #d9894a;
    --photo-mid: #9a5a2e;
    --photo-dark: #3b2416;
    --title-box: rgba(110, 70, 48, 0.72);
    --text-light: #ffffff;
    --brand-text: #8b90a6;
    --brand-dot: #f0603a;
    --card-dark-a: #2c2d31;
    --card-dark-b: #6b6d73;
    --card-gold-a: #c7a866;
    --card-gold-b: #efe0b4;
  }
  html, body {
    margin: 0;
    padding: 0;
    width: 1200px;
    height: 1200px;
    overflow: hidden;
    background: var(--page-bg);
  }
  .canvas {
    position: relative;
    width: 1200px;
    height: 1200px;
  }
  .banner {
    position: absolute;
    left: 148px;
    top: 300px;
    width: 906px;
    height: 606px;
    overflow: hidden;
    font-family: "Montserrat", Arial, sans-serif;
  }
  .banner__photo {
    position: absolute;
    inset: 0;
    background:
      radial-gradient(ellipse 30% 40% at 56% 62%, rgba(240, 190, 140, 0.55), transparent 70%),
      radial-gradient(ellipse 60% 70% at 45% 35%, var(--photo-light), transparent 75%),
      linear-gradient(100deg, var(--photo-dark) 0%, var(--photo-mid) 35%, var(--photo-mid) 65%, var(--photo-dark) 100%);
  }
  .headline-box {
    position: absolute;
    left: 0;
    top: 32px;
    width: 720px;
    height: 174px;
    background: var(--title-box);
  }
  .headline {
    position: absolute;
    left: 50px;
    top: 42px;
    margin: 0;
    color: var(--text-light);
    font-weight: 600;
    font-size: 58px;
    line-height: 65px;
    letter-spacing: 0.5px;
  }
  .tagline {
    position: absolute;
    left: 56px;
    top: 256px;
    margin: 0;
    color: var(--text-light);
    font-weight: 700;
    font-size: 30px;
    line-height: 41px;
  }
  .brand {
    position: absolute;
    left: 58px;
    top: 528px;
    display: flex;
    align-items: center;
    gap: 10px;
  }
  .brand__dot {
    width: 22px;
    height: 22px;
    border-radius: 50%;
    background: var(--brand-dot);
  }
  .brand__name {
    color: var(--brand-text);
    font-weight: 700;
    font-size: 25px;
  }
  .card {
    position: absolute;
    width: 234px;
    height: 147px;
    border-radius: 10px;
  }
  .card--gold {
    left: 626px;
    top: 394px;
    background: linear-gradient(135deg, var(--card-gold-a), var(--card-gold-b) 55%, var(--card-gold-a));
  }
  .card--dark {
    left: 584px;
    top: 438px;
    background: linear-gradient(135deg, var(--card-dark-a), var(--card-dark-b) 60%, var(--card-dark-a));
    box-shadow: 0 4px 10px rgba(0, 0, 0, 0.35);
  }
</style>
</head>
<body>
<div class="canvas">
  <section class="banner">
    <div class="banner__photo" role="img" aria-label="Foto di una ragazza di spalle con le braccia alzate in una strada illuminata da luci calde"></div>

    <div class="headline-box"></div>
    <h1 class="headline">All in One !<br>Una carta per tutti</h1>

    <p class="tagline">Enjoy your cart!<br>Fai quello che vuoi,<br>Nessun limite.<br>Nessun controllo.</p>

    <div class="brand">
      <span class="brand__dot"></span>
      <span class="brand__name">PagaVelo</span>
    </div>

    <div class="card card--gold" role="img" aria-label="Carta di debito dorata"></div>
    <div class="card card--dark" role="img" aria-label="Carta di debito nera"></div>
  </section>
</div>
</body>
</html>
```